Safety glasses retailer needs new A5 and A4 flyers

We need two new double sided A5 and A4 flyers to send out with our safety glasses and drawing boards. We sell to many different professionals who work in construction, planning and designing. The flyers will give basic details about our products (safety glasses, drawing boards and plastic frame packers) and encourage the customer to go to our website to obtain further information.
We want the flyers to look as professional as possible without being too boring!
European sstandard sizes A4 & A5
Builders, surveyors, architect, tradespeople, cyclists, bikers
Plastic

```html
<!DOCTYPE html>
<html lang="en">
<head>
<meta charset="utf-8">
<title>LineMate Drafter flyer</title>
<link rel="stylesheet" href="https://fonts.googleapis.com/css2?family=Russo+One&family=Exo+2:wght@400;500;700&display=swap">
<style>
  :root {
    --orange: #f0901a;
    --orange-deep: #d96f0c;
    --amber: #f7b21e;
    --ink: #2b2b2b;
    --body: #3a3a3a;
    --cream: #f7efe4;
    --paper: #fdfaf6;
    --white: #ffffff;
  }
  * { box-sizing: border-box; margin: 0; padding: 0; }
  html, body { width: 1200px; height: 848px; overflow: hidden; background: var(--paper); }
  .flyer {
    position: relative; width: 1200px; height: 848px; overflow: hidden;
    background: radial-gradient(ellipse at 70% 40%, var(--white) 0%, var(--paper) 45%, var(--cream) 100%);
    font-family: "Exo 2", sans-serif; color: var(--body);
  }
  .deco { position: absolute; }
  .deco-top-left { left: 0; top: 0; width: 960px; height: 640px; }
  .deco-right { right: 0; top: 250px; width: 90px; height: 420px; }

  .headline { position: absolute; left: 0; top: 110px; }
  .headline-line {
    display: block; height: 52px; margin-bottom: 5px;
    padding-left: 70px; padding-right: 14px;
    background: linear-gradient(90deg, var(--orange) 0%, var(--amber) 100%);
    font-family: "Russo One", sans-serif; font-size: 44px; line-height: 54px;
    color: var(--ink); text-transform: uppercase; letter-spacing: 0.5px;
    text-shadow: 2px 2px 0 var(--white);
    width: max-content;
  }

  .intro {
    position: absolute; left: 66px; top: 358px; width: 395px;
    padding: 6px 0 7px; border-top: 2px solid var(--orange); border-bottom: 2px solid var(--orange);
    font-size: 20px; line-height: 24px; color: var(--ink); white-space: nowrap;
  }

  .hatch {
    position: absolute; height: 14px;
    background: repeating-linear-gradient(115deg, var(--orange) 0 3px, transparent 3px 8px);
  }
  .hatch-left { left: 80px; top: 538px; width: 320px; }
  .hatch-bottom { left: 463px; top: 748px; width: 300px; height: 10px; }

  .features { position: absolute; left: 80px; top: 598px; list-style: none; width: 380px; }
  .features li {
    position: relative; padding-left: 24px; font-size: 16px; line-height: 21px; margin-bottom: 6px;
  }
  .features li::before {
    content: ""; position: absolute; left: 0; top: 4px; width: 13px; height: 13px;
    background: linear-gradient(135deg, var(--amber) 50%, var(--orange-deep) 50%);
  }

  .brand {
    position: absolute; left: 860px; top: 108px;
    font-family: "Exo 2", sans-serif; font-weight: 500; font-size: 34px; line-height: 38px;
    color: var(--orange-deep); text-transform: uppercase; text-align: right;
    display: flex; align-items: center; gap: 12px;
  }
  .brand-mark { width: 18px; height: 18px; border-radius: 50%; background: var(--orange-deep); }

  .product-photo {
    position: absolute; left: 478px; top: 216px; width: 660px; height: 487px;
    background: linear-gradient(160deg, #e9e9ea 0%, #cfd3d6 40%, #3b3b3e 75%, #2a2a2c 100%);
    border-radius: 4px;
  }

  .callout {
    position: absolute; background: var(--orange); color: var(--white);
    font-family: "Exo 2", sans-serif; font-weight: 700; text-transform: uppercase;
    text-align: center; font-size: 16px; line-height: 19px;
    display: flex; align-items: center; justify-content: center;
  }
  .callout-protractor {
    left: 404px; top: 506px; width: 242px; height: 96px;
    clip-path: polygon(4% 0, 100% 0, 94% 100%, 0 100%);
  }
  .callout-grid {
    left: 880px; top: 640px; width: 236px; height: 86px;
    clip-path: polygon(0 0, 100% 10%, 96% 100%, 4% 92%);
  }

  .dotted-rule {
    position: absolute; left: 594px; top: 690px; width: 280px; height: 6px;
    background: repeating-linear-gradient(90deg, var(--orange) 0 3px, transparent 3px 6px);
  }

  .web-bar {
    position: absolute; left: 454px; top: 768px; width: 740px; height: 36px;
    background: var(--orange); color: var(--white);
    font-size: 18px; line-height: 36px; padding-left: 20px;
  }
  .web-bar strong { font-weight: 700; }
</style>
</head>
<body>
<main class="flyer">
  <svg class="deco deco-top-left" viewBox="0 0 960 640" role="img" aria-label="Orange low-poly geometric decoration">
    <defs>
      <linearGradient id="polyTone" x1="0" y1="0" x2="1" y2="1">
        <stop offset="0" stop-color="#f7a52a"/>
        <stop offset="1" stop-color="#d96f0c"/>
      </linearGradient>
    </defs>
    <polygon points="0,0 450,0 480,60 330,110 420,250 170,310 0,250" fill="url(#polyTone)" opacity="0.9"/>
    <polygon points="140,0 300,0 230,90" fill="#e07d12" opacity="0.8"/>
  </svg>
  <svg class="deco deco-right" viewBox="0 0 90 420" role="img" aria-label="Orange low-poly geometric decoration">
    <polygon points="90,0 20,90 50,200 0,330 90,420" fill="#e5820f" opacity="0.85"/>
  </svg>

  <h1 class="headline">
    <span class="headline-line">The LineMate Drafter</span>
    <span class="headline-line">Draw straight lines</span>
    <span class="headline-line">Totally free</span>
  </h1>

  <p class="intro">It’s never been so easy to draw<br>perfect straight lines FREEHAND.<br>Just place the LineMate Drafter<br>sheet under your paper and draw<br>perfect straight lines everytime!</p>

  <div class="hatch hatch-left"></div>

  <ul class="features">
    <li>Has Microscopic pyramids on the surface that enable you to draw straight lines</li>
    <li>Used by builders, engineers, surveyors, floorplaners, designers and many more...</li>
    <li>No special pen or paper needed</li>
    <li>Can be used for scale drawings</li>
    <li>Easy to use and saves time</li>
    <li>Amaze your customers</li>
  </ul>

  <div class="brand"><span class="brand-mark"></span><span>LineMate<br>Drafter</span></div>

  <div class="product-photo" role="img" aria-label="Photo of the drafting kit: clear protractor sheet with ruler, instruction card and a black folder holding a gridded sheet with a pencil"></div>

  <div class="callout callout-protractor">Protractor sheet<br>can be used to<br>draw lines<br>at angles</div>
  <div class="callout callout-grid">Gridded sheet<br>can be used for<br>scale drawings</div>

  <div class="dotted-rule"></div>
  <div class="hatch hatch-bottom"></div>

  <div class="web-bar">See the full range of LineMate Drafter products at <strong>www.truelineboards.com</strong></div>
</main>
</body>
</html>
```